Vantrell Law Letterhead

We need a new letterhead design for a Law Firm. The address for the law firm is 4817 Larkspur Boulevard, Suite 250, Houston, Texas 77342. Phone Number: 832-619-3057; Fax Number: 832-407-1694. The logo is uploaded to the project.

```html
<!DOCTYPE html>
<html lang="en">
<head>
<meta charset="utf-8">
<title>Vantrell Law Letterhead</title>
<link rel="stylesheet" href="https://fonts.googleapis.com/css2?family=Montserrat:wght@300;400;500;600&display=swap">
<style>
  :root {
    --backdrop: #e9e9ea;
    --paper: #ffffff;
    --navy: #162a56;
    --red: #cc1c24;
    --ink: #3a3a3c;
    --rule: #9aa3b8;
  }
  * { margin: 0; padding: 0; box-sizing: border-box; }
  html, body {
    width: 1200px; height: 898px; overflow: hidden;
    background: var(--backdrop);
    font-family: "Montserrat", sans-serif;
  }
  .letterhead {
    position: absolute; left: 303px; top: 29px;
    width: 594px; height: 840px;
    background: var(--paper);
    box-shadow: 0 6px 24px rgba(0,0,0,0.12);
    overflow: hidden;
  }
  .corner-accent { position: absolute; left: 0; top: 0; }
  .brand {
    position: absolute; left: 0; right: 0; top: 78px;
    display: flex; justify-content: center; align-items: center; gap: 12px;
  }
  .brand-mark { width: 30px; height: 30px; border-radius: 50%; background: var(--navy); }
  .brand-name {
    font-weight: 600; font-size: 30px; color: var(--navy); letter-spacing: 0.5px;
  }
  .tagline {
    position: absolute; left: 0; right: 0; top: 122px; text-align: center;
    font-size: 7px; letter-spacing: 1.6px; text-transform: uppercase; color: var(--red);
  }
  .letter-body {
    position: absolute; left: 110px; right: 70px; top: 200px;
    font-size: 9px; line-height: 1.7; font-weight: 400; color: var(--ink);
  }
  .letter-body p { margin-bottom: 16px; }
  .closing {
    position: absolute; left: 448px; top: 500px; font-size: 9px; color: var(--ink);
  }
  .signature {
    position: absolute; left: 452px; top: 520px; width: 60px; height: 36px;
    background: linear-gradient(#f4f4f5, #ececee);
  }
  .footer-band {
    position: absolute; right: 0; bottom: 0; width: 225px; height: 66px;
    background: var(--navy);
    display: flex; align-items: center; justify-content: flex-end; padding-right: 20px;
  }
  .footer-band .band-name { color: #fff; font-weight: 600; font-size: 13px; }
  .contact {
    position: absolute; bottom: 40px; font-size: 8.5px; font-weight: 500;
    color: var(--navy); line-height: 1.45;
  }
  .contact-address { left: 96px; display: flex; gap: 5px; }
  .contact-phones { left: 292px; bottom: 60px; }
  .contact-phones div { display: flex; gap: 5px; align-items: center; }
  .contact-divider {
    position: absolute; left: 262px; bottom: 38px; width: 1px; height: 40px; background: var(--rule);
  }
  .icon { width: 8px; height: 8px; flex: none; margin-top: 2px; }
</style>
</head>
<body>
  <main class="letterhead">
    <svg class="corner-accent" width="112" height="128" viewBox="0 0 112 128">
      <polygon points="0,0 112,0 0,128" fill="var(--red)"/>
    </svg>

    <header>
      <div class="brand">
        <span class="brand-mark"></span>
        <span class="brand-name">Vantrell Law</span>
      </div>
      <div class="tagline">Your recovery is our first priority</div>
    </header>

    <section class="letter-body">
      <p>Lorem ipsum dolor sit amet, consectetur adipiscing elit. Donec orci purus, luctus vitae dignissim eu, iaculis sed purus. Vivamus faucibus, ipsum nec aliquet viverra, leo mauris condimentum ligula, sit amet sagittis enim ligula quis arcu. Nam egestas tortor id nisi porttitor mattis. In tortor ante, ultricies in suscipit a, tempus non massa. Vivamus et auctor mi. Fusce vel massa nulla. Phasellus nec eros mauris, et scelerisque orci.</p>
      <p>Donec malesuada orci vitae nulla accumsan porta a id massa. Quisque accumsan iaculis magna sit amet fringilla. Maecenas consequat, magna eget tincidunt semper, odio nibh rutrum mi, id feugiat ante nisi eu risus. Vestibulum nunc orci, rhoncus a placerat in, ultricies in mi. Cras mattis varius eros, vel fringilla nisi suscipit eget. Quisque scelerisque sagittis nulla at porttitor.</p>
      <p>Sed id augue vitae urna euismod commodo aliquet a quam. Pellentesque arcu velit, cursus et malesuada ut, consequat et diam. Nullam erat sem, rhoncus id ullamcorper vitae, rhoncus et arcu. In ultricies ultricies nulla, ut rutrum nisi iaculis at. Donec eu magna a metus ornare faucibus. Fusce aliquet faucibus ultricies. Morbi semper, est id tincidunt gravida, sem arcu adipiscing lacus, ac bibendum nulla leo eu purus. Quisque nec diam sed risus consectetur a ccumsan quis quis nibh. Vestibulum id purus lorem.</p>
    </section>

    <div class="closing">Sincerily,</div>
    <div class="signature" role="img" aria-label="Handwritten signature of the attorney"></div>

    <footer>
      <div class="contact contact-address">
        <svg class="icon" viewBox="0 0 10 10"><path d="M5 0.5a3.2 3.2 0 0 0-3.2 3.2C1.8 6 5 9.5 5 9.5S8.2 6 8.2 3.7A3.2 3.2 0 0 0 5 0.5zm0 4.5a1.3 1.3 0 1 1 0-2.6 1.3 1.3 0 0 1 0 2.6z" fill="var(--navy)"/></svg>
        <span>4817 Larkspur Boulevard,<br>Suite 250, Houston,<br>Texas 77342.</span>
      </div>
      <div class="contact-divider"></div>
      <div class="contact contact-phones">
        <div>
          <svg class="icon" viewBox="0 0 10 10"><path d="M2.2 0.8l1.5 1.8-0.9 1.1c0.6 1.2 1.5 2.1 2.6 2.6l1.1-0.9 1.8 1.5-0.8 1.6C4.3 8.3 1.4 5.4 0.8 1.6z" fill="var(--navy)"/></svg>
          <span>832-619-3057</span>
        </div>
        <div>
          <svg class="icon" viewBox="0 0 10 10"><rect x="2.5" y="0.8" width="5" height="2.6" fill="none" stroke="var(--navy)"/><rect x="0.8" y="3.4" width="8.4" height="3.8" rx="0.8" fill="none" stroke="var(--navy)"/><rect x="2.5" y="6" width="5" height="3" fill="none" stroke="var(--navy)"/></svg>
          <span>832-407-1694</span>
        </div>
      </div>
      <div class="footer-band"><span class="band-name">Vantrell Law</span></div>
    </footer>
  </main>
</body>
</html>
```